Veranthex LLC, providing clean, low emission fuel for the transport and maritime industry

Veranthex LLC is a Texas based company dedicated to the development of Small Scale LNG projects with the objective of supplying clean, low emission fuel to the transport and maritime industry.

The design should be simple and sophisticated. We want a design that includes our company logo and uses our company logo colors. The site should include 7 pages (Home, About, What is LNG, Projects, Announcements and Contact Us). The site should ultimately be editable and capable of being imported into ZUMO. The design should communicate an environmentally conscious company who provide "Simple, Practical, and Cost Effective Solutions". Our competitions website looks like this www.harbvexa.com.

Target Market(s)

LNG, maritime

Industry/Entity Type

Oil And Gas

Coding

Number of Pages Required

Requirements
Must have
• Equal or better than our competitors website www.harbvexa.com
Company Logo.
The tagline "Simple, Practical, and Cost Effective Solutions"
Nice to have
• The page content will be very similar to our competitors website www.harbvexa.com
Should not have
• No red or black colours.

```html
<!DOCTYPE html>
<html lang="en">
<head>
<meta charset="utf-8">
<title>Veranthex LLC</title>
<link rel="stylesheet" href="https://fonts.googleapis.com/css2?family=Play:wght@400;700&family=Open+Sans:wght@400;600&family=Roboto:wght@400&display=swap">
<style>
:root{
  --navy:#163f87;
  --deep-navy:#0e3a85;
  --green:#3a8a2e;
  --button-green:#3e8d32;
  --grad-blue:#174f93;
  --grad-green:#2f8a3b;
  --grad-teal:#1478a9;
  --mist:#e6edf1;
  --text:#3a3a3a;
  --muted:#6d6d6d;
  --white:#ffffff;
}
*{box-sizing:border-box;margin:0;padding:0}
html,body{width:1200px;height:3101px;overflow:hidden;background:var(--white)}
body{position:relative;font-family:"Open Sans",sans-serif;color:var(--text)}
.abs{position:absolute}
.heading{font-family:"Play",sans-serif;font-weight:700;text-transform:uppercase}
.btn{position:absolute;display:flex;align-items:center;justify-content:center;font-family:"Play",sans-serif;font-weight:700;color:var(--white);background:var(--button-green);text-transform:uppercase;font-size:17px;text-decoration:none}

/* header */
.site-header{position:absolute;left:0;top:0;width:1200px;height:89px;background:var(--white)}
.brand{position:absolute;left:82px;top:23px;display:flex;align-items:center;gap:12px}
.brand-dot{width:42px;height:42px;border-radius:50%;background:var(--navy)}
.brand-name{font-family:"Play",sans-serif;font-weight:700;font-size:28px;color:var(--navy);letter-spacing:1px}
.main-nav a{position:absolute;top:40px;font-family:"Play",sans-serif;font-weight:700;font-size:15px;color:var(--navy);text-decoration:none}
.main-nav a.active{color:var(--green)}

/* hero */
.hero{position:absolute;left:0;top:89px;width:1200px;height:572px;background:linear-gradient(120deg,#1c4d66 0%,#24607e 35%,#3573a6 55%,#3f86b8 72%,#1f5273 100%)}
.hero-title{position:absolute;left:0;width:1200px;text-align:center;color:var(--white);font-family:"Play",sans-serif;font-size:43px;line-height:50px}
.hero-title.strong{top:172px;font-weight:700}
.hero-title.light{top:224px;font-weight:400}
.hero-dots span{position:absolute;left:1144px;width:14px;height:14px;border-radius:50%;background:var(--white)}
.hero-dots span.current{background:transparent;border:2px solid var(--white)}

/* welcome */
.welcome{position:absolute;left:0;top:661px;width:1200px;height:407px;background:linear-gradient(100deg,var(--grad-blue) 0%,#1f6a72 55%,var(--grad-green) 100%);color:var(--white);text-align:center}
.welcome h1{position:absolute;top:84px;width:1200px;font-size:34px}
.welcome p{position:absolute;left:195px;width:810px;font-size:15px;line-height:23px}

/* about */
.about-art{position:absolute;left:186px;top:1148px;width:285px;height:375px;background:linear-gradient(170deg,#c89a5e 0%,#b9874f 30%,#2f5c9a 62%,#8a6a4a 100%)}
.section-title{position:absolute;font-size:34px;line-height:40px}
.section-title .accent{color:var(--green)}
.section-title .main{color:var(--navy)}
.body-copy{position:absolute;font-size:15px;line-height:23.5px;color:var(--text)}

/* lng */
.lng{position:absolute;left:0;top:1610px;width:1200px;height:513px;background:var(--mist)}
.photo{background:linear-gradient(160deg,#3d6fae 0%,#8fb0d6 35%,#d97a3a 60%,#2d4a6f 100%)}

/* projects */
.project-card{position:absolute;top:2253px;width:294px;height:316px;background:var(--white);box-shadow:0 1px 4px rgba(0,0,0,.25)}
.project-photo{width:294px;height:188px}
.project-card h3{position:absolute;left:28px;top:212px;font-family:"Roboto",sans-serif;font-weight:400;font-size:22px;color:var(--green)}
.project-card p{position:absolute;left:28px;top:254px;width:250px;font-family:"Roboto",sans-serif;font-size:13px;line-height:17px;color:var(--muted)}

/* contact band */
.contact-band{position:absolute;left:0;top:2634px;width:1200px;height:353px;background:linear-gradient(100deg,var(--grad-green) 0%,#23806a 50%,var(--grad-teal) 100%);color:var(--white)}
.contact-band h2{position:absolute;left:142px;top:122px;font-size:40px}
.contact-band p{position:absolute;left:142px;top:175px;font-family:"Roboto",sans-serif;font-size:17px}
.contact-band .btn{left:828px;top:137px;width:219px;height:58px;background:var(--deep-navy);font-size:18px}

/* footer */
.site-footer{position:absolute;left:0;top:2987px;width:1200px;height:114px;font-size:15px;color:var(--text)}
.social span{position:absolute;top:43px;width:20px;height:20px;border-radius:50%;background:var(--navy)}
.legal{position:absolute;left:865px;top:40px}
</style>
</head>
<body>

<header class="site-header">
  <div class="brand"><span class="brand-dot"></span><span class="brand-name">VERANTHEX</span></div>
  <nav class="main-nav">
    <a class="active" style="left:384px">HOME</a>
    <a style="left:468px">ABOUT</a>
    <a style="left:561px">WHAT IS LNG</a>
    <a style="left:694px">PROJECTS</a>
    <a style="left:812px">ANNOUNCEMENTS</a>
    <a style="left:987px">CONTACT US</a>
  </nav>
</header>

<section class="hero" role="img" aria-label="Aerial view of a container ship loaded with colourful containers on the sea">
  <div class="hero-title strong">SIMPLE, PRACTICAL, AND COST</div>
  <div class="hero-title light">EFFECTIVE SOLUTIONS</div>
  <a class="btn" style="left:503px;top:289px;width:185px;height:53px">Learn More</a>
  <div class="hero-dots">
    <span class="current" style="top:221px"></span>
    <span style="top:242px"></span>
    <span style="top:264px"></span>
    <span style="top:287px"></span>
  </div>
</section>

<section class="welcome">
  <h1 class="heading">Welcome to Veranthex LLC</h1>
  <p style="top:158px">Veranthex ultricies orci ac feugiat suscipit leo massa sodales velit et scelerisque mi tortor at ipsum Proin orci odio commodo ac gravida non tristique vel te Curabitur iaculis tempus eros Curabitur vel mi sit amet magna malesuada ultrices Ut nisi erat fermentum vel congue id euismod in elit</p>
  <p style="top:241px">Fusce ultricies orci ac feugiat suscipit leo massa sodales velit et scelerisque quam Curabitur vel dolor ultrices ipsum dictum tristique Praesent vitae lacus Ut velit enim vestibulum non fermentum</p>
</section>

<div class="about-art" role="img" aria-label="Collage of a container terminal with port cranes and cargo ships"></div>
<h2 class="section-title heading" style="left:602px;top:1197px"><span class="accent">About</span> <span class="main">Veranthex LLC</span></h2>
<p class="body-copy" style="left:602px;top:1264px;width:505px">Aultricies orci ac feugiat suscipit leo massa sodales velit et scelerisque mi tortor at ipsum Proin orci odio commodo ac gravida non tristique vel te Curabitur iaculis tempus eros Curabitur vel mi sit amet</p>
<p class="body-copy" style="left:602px;top:1360px;width:505px">Aagna malesuada ultrices Ut nisi erat fermentum vel congue id euismod in elit Fusce ultricies orci ac feugiat suscipit leo</p>
<a class="btn" style="left:602px;top:1443px;width:173px;height:51px">Learn More</a>

<section class="lng">
  <h2 class="section-title heading" style="left:136px;top:116px"><span class="accent">What is</span> <span class="main">LNG</span></h2>
  <p class="body-copy" style="left:136px;top:181px;width:445px">Aultricies orci ac feugiat suscipit leo massa sodales velit et scelerisque mi tortor at ipsum Proin orci odio commodo ac gravida non tristique vel te Curabitur iaculis tempus eros Aagna malesuada ultrices Ut nisi erat fermentum vel congue id euismod in elit Fusce ultricies orci ac</p>
  <a class="btn" style="left:136px;top:336px;width:175px;height:51px">Learn More</a>
  <div class="abs photo" style="left:622px;top:89px;width:447px;height:312px" role="img" aria-label="Orange port cranes loading a container ship under a blue sky"></div>
</section>

<h2 class="section-title heading" style="left:141px;top:2180px"><span class="accent">Latest</span> <span class="main">Projects</span></h2>
<article class="project-card" style="left:136px">
  <div class="project-photo" style="background:linear-gradient(180deg,#2e5a92,#4f7fb5 60%,#e8eef4)" role="img" aria-label="White cruise ship sailing on blue sea"></div>
  <h3>Project Title here</h3>
  <p>eros Curabitur vel mi sit amet magna malesuada ultrices Ut nisi erat</p>
</article>
<article class="project-card" style="left:462px">
  <div class="project-photo" style="background:linear-gradient(150deg,#1d4f9a,#6c86b3 50%,#c9ced6)" role="img" aria-label="Cylindrical LNG storage tank with spiral staircase"></div>
  <h3>Project Title here</h3>
  <p>eros Curabitur vel mi sit amet magna malesuada ultrices Ut nisi erat</p>
</article>
<article class="project-card" style="left:782px">
  <div class="project-photo" style="background:linear-gradient(150deg,#1f7f8f,#2a9aa6 50%,#d98a3e)" role="img" aria-label="Container ship loaded with containers on turquoise water"></div>
  <h3>Project Title here</h3>
  <p>eros Curabitur vel mi sit amet magna malesuada ultrices Ut nisi erat</p>
</article>

<section class="contact-band">
  <h2 class="heading">Contact Us Now</h2>
  <p>Augiat in pede Fusce tellus Sed metus augue convallis et vehicula ut pulvinar</p>
  <a class="btn">Contact Us</a>
</section>

<footer class="site-footer">
  <div class="abs" style="left:140px;top:40px">© 2020 Company Name | All Rights Reserved</div>
  <div class="social">
    <span style="left:547px"></span>
    <span style="left:603px"></span>
    <span style="left:657px"></span>
  </div>
  <div class="legal">Term of Use &nbsp;|&nbsp; Privacy Policy</div>
</footer>

</body>
</html>
```